Feminine colorfull packaging for coconut skin care brand

We need a design that can be used on different types of packaging for beauty products likes creams, oils, etc.
The products that we will launch will be made with one key ingredient of coconut oil + other added ingredients depending on the type of product. The entire marketing will therefore be based on COCONUTS, palmtrees, sand, beach, bronzing on the beach, holiday feeling, nature, femininity, etc. = A Lifestyle brand with a tropical vibe.
Packaging can be a pot for creams, flaskes for lotions, smaller bottles for oils, etc. Mostly the standard packaging used for beauty products.
We would like to use the color pink ( this can be bright or pastel or any tone of pink) to address the feminine side of our product and a tone of blue-green ( pastel, bright or any tone of this color) to accentuate the use of coconut.
Third would be the color white (this can be added through an accent somewhere on the packaging or this can be the brand name that is written in white)
Lastely we would like the packaging to be light, fresh and playfull. Please feel free to use different colors or shapes ( we do not yet have a logo. This can then be designed followed on the packaging)
The design will be printed on plastic packaging. We are open to very creative designs. We are looking for packaging that catches the eye by its design and/or colors, that is different than others, that distinguishes the product because of its packaging design.
Target Market(s)
Women between 20 - 35 years
Industry/Entity Type
Beauty
Colors
Designer to choose colors to be used in the design.
Look and feel

```html
<!DOCTYPE html>
<html lang="en">
<head>
<meta charset="utf-8">
<title>Laguna – Skin Care Packaging Labels</title>
<link rel="stylesheet" href="https://fonts.googleapis.com/css2?family=Montserrat:wght@400;500&display=swap">
<style>
  :root {
    --backdrop: #a7cfd0;
    --label-white: #ffffff;
    --label-cream: #fbf6ec;
    --blush: #f7d3ea;
    --pink: #ef8fd9;
    --magenta: #e04fcf;
    --ink: #141414;
    --soft-ink: #2a2a2a;
  }
  * { box-sizing: border-box; margin: 0; padding: 0; }
  html, body { width: 1200px; height: 800px; overflow: hidden; }
  body {
    background: var(--backdrop);
    font-family: "Montserrat", sans-serif;
    color: var(--ink);
  }
  .label-sheet {
    width: 1200px; height: 800px;
    display: flex; align-items: flex-end; justify-content: center;
    gap: 40px; padding-bottom: 130px;
  }
  .label {
    position: relative; overflow: hidden;
    background: linear-gradient(180deg, var(--label-white) 0%, var(--label-cream) 35%, var(--blush) 65%, var(--pink) 100%);
    box-shadow: 0 6px 18px rgba(40, 80, 80, 0.18);
    display: flex; flex-direction: column; align-items: center;
  }
  .label__waves { position: absolute; left: 0; bottom: 0; width: 100%; height: 45%; }
  .label__content { position: relative; display: flex; flex-direction: column; align-items: center; text-align: center; }
  .brand { display: flex; align-items: center; gap: 8px; font-weight: 400; color: var(--ink); letter-spacing: 0.04em; }
  .brand__dot { border-radius: 50%; background: var(--ink); }
  .product-name { font-weight: 500; letter-spacing: 0.1em; color: var(--soft-ink); text-transform: uppercase; line-height: 1.45; }
  .volume { font-weight: 400; color: var(--soft-ink); letter-spacing: 0.04em; }

  /* tube */
  .label--tube { width: 230px; height: 420px; border-radius: 4px; }
  .label--tube .volume { font-size: 11px; margin-top: 10px; }
  .label--tube .brand { font-size: 34px; margin-top: 80px; }
  .label--tube .brand__dot { width: 12px; height: 12px; }
  .label--tube .product-name { font-size: 14px; margin-top: 50px; }

  /* jar */
  .label--jar { width: 300px; height: 170px; border-radius: 6px; }
  .label--jar .label__content { width: 100%; height: 100%; justify-content: center; }
  .label--jar .brand { font-size: 26px; }
  .label--jar .brand__dot { width: 9px; height: 9px; }
  .label--jar .product-name { position: absolute; left: 18px; top: 118px; font-size: 9px; text-align: left; }
  .label--jar .volume { position: absolute; right: 24px; top: 122px; font-size: 11px; }

  /* cleanser bottle */
  .label--bottle { width: 270px; height: 400px; border-radius: 60px 60px 6px 6px; }
  .label--bottle .brand { font-size: 36px; margin-top: 130px; }
  .label--bottle .brand__dot { width: 12px; height: 12px; }
  .label--bottle .product-name { font-size: 18px; margin-top: 70px; }
  .label--bottle .volume { font-size: 14px; margin-top: 70px; }

  /* oil dropper */
  .label--dropper { width: 130px; height: 200px; border-radius: 18px 18px 6px 6px; }
  .label--dropper .brand { font-size: 18px; margin-top: 42px; gap: 5px; }
  .label--dropper .brand__dot { width: 6px; height: 6px; }
  .label--dropper .product-name { font-size: 10px; margin-top: 22px; }
  .label--dropper .volume { font-size: 9px; margin-top: 28px; }
</style>
</head>
<body>
<main class="label-sheet">

  <section class="label label--tube" aria-label="Anti-aging skin care cream tube label">
    <svg class="label__waves" viewBox="0 0 230 190" preserveAspectRatio="none" aria-hidden="true">
      <path d="M0 70 C60 20 140 120 230 40 L230 190 L0 190 Z" fill="var(--pink)" opacity="0.55"/>
      <path d="M0 120 C70 70 150 160 230 100 L230 190 L0 190 Z" fill="var(--magenta)" opacity="0.55"/>
    </svg>
    <div class="label__content">
      <p class="volume">150ml e</p>
      <h2 class="brand"><span class="brand__dot"></span>LAGUNA</h2>
      <p class="product-name">Anti-Aging<br>Skin Care Cream</p>
    </div>
  </section>

  <section class="label label--jar" aria-label="Hand cream jar label">
    <svg class="label__waves" viewBox="0 0 300 80" preserveAspectRatio="none" aria-hidden="true">
      <path d="M0 40 C80 5 180 70 300 20 L300 80 L0 80 Z" fill="var(--pink)" opacity="0.6"/>
      <path d="M0 65 C90 40 200 85 300 55 L300 80 L0 80 Z" fill="var(--magenta)" opacity="0.55"/>
    </svg>
    <div class="label__content">
      <h2 class="brand"><span class="brand__dot"></span>LAGUNA</h2>
      <p class="product-name">Hand<br>Cream</p>
      <p class="volume">300ml e</p>
    </div>
  </section>

  <section class="label label--bottle" aria-label="Gentle skin cleanser bottle label">
    <svg class="label__waves" viewBox="0 0 270 180" preserveAspectRatio="none" aria-hidden="true">
      <path d="M0 80 C80 30 170 130 270 50 L270 180 L0 180 Z" fill="var(--pink)" opacity="0.55"/>
      <path d="M0 135 C90 90 180 170 270 110 L270 180 L0 180 Z" fill="var(--magenta)" opacity="0.5"/>
    </svg>
    <div class="label__content">
      <h2 class="brand"><span class="brand__dot"></span>LAGUNA</h2>
      <p class="product-name">Gentle Skin<br>Cleanser</p>
      <p class="volume">300ml e</p>
    </div>
  </section>

  <section class="label label--dropper" aria-label="Skincare oil dropper bottle label">
    <svg class="label__waves" viewBox="0 0 130 90" preserveAspectRatio="none" aria-hidden="true">
      <path d="M0 45 C40 15 90 70 130 30 L130 90 L0 90 Z" fill="var(--pink)" opacity="0.6"/>
      <path d="M0 70 C45 50 90 90 130 60 L130 90 L0 90 Z" fill="var(--magenta)" opacity="0.55"/>
    </svg>
    <div class="label__content">
      <h2 class="brand"><span class="brand__dot"></span>LAGUNA</h2>
      <p class="product-name">Skincare<br>Oil</p>
      <p class="volume">300ml e</p>
    </div>
  </section>

</main>
</body>
</html>
```